Aggressive Inline Skaten für Jugendliche/Kids in Öhringen
Zielgruppe
Meine Zielgruppe sind Kids/Jugendliche. Und die Extrem Sportart "Aggressive Inline Skating" soll von einem professionellen Trainer beigebracht werden.
Aufgabenstellung
Aggressive Inline Skating muss auf jeden Fall rein und das es ein professionelles Training gibt. Preise werden nicht angegeben, da es eine Facharbeit wird und ich noch kein Controlling hatte. Kontaktdaten könnte man evt. einbeziehen falls es von Vorteil ist.
E-Mail Adresse, die Fotos könnte man auch bearbeiten und miteinfügen, es sollte einseitig werden und ein handlicher Flyer werden, der gut überschaubar ist. Also größer wie (Höhe=20cm;Breite=13cm) sollte er nicht sein und evt. vielleicht in der Größe (Höhe=15cm;Breite=10,5). Natürlich kann der Designer aber frei wählen. Und diese Extremsportart wird von einem professionellen Trainer durchgeführt und ist für Kinder und Jugendliche. Ein genaue Altersdefinierung gibt es nicht. Auch könnte man eine Linkverweisung auf Flimmora machen, da es dort aggressive Inline Videos gibt und es ein direkten Bezug gibt, um die Sportart zu zeigen.

```html
<!DOCTYPE html>
<html lang="de">
<head>
<meta charset="utf-8">
<title>Aggressive Inline Skating – Flyer</title>
<link rel="stylesheet" href="https://fonts.googleapis.com/css2?family=Josefin+Sans:wght@300;400;600&family=Montserrat:wght@500;700&display=swap">
<style>
  :root {
    --bg: #1f2327;
    --bg-deep: #181b1e;
    --accent: #2fa6ea;
    --accent-light: #6fd0ff;
    --accent-dark: #1673c4;
    --text: #f4f6f8;
    --text-soft: #d6dde3;
    --sky-top: #8cc3ec;
    --sky-mid: #cfe3f4;
    --trees: #35513a;
    --ramp: #8d959c;
  }
  * { margin: 0; padding: 0; box-sizing: border-box; }
  html, body { width: 840px; height: 1200px; overflow: hidden; background: var(--bg); }
  .flyer {
    position: relative;
    width: 840px; height: 1200px;
    background: radial-gradient(ellipse at 50% 40%, #262b30 0%, var(--bg) 55%, var(--bg-deep) 100%);
    overflow: hidden;
    font-family: "Josefin Sans", sans-serif;
    color: var(--text);
  }
  .edge-bar {
    position: absolute; left: 0; width: 100%; height: 6px;
    background: linear-gradient(90deg, var(--accent-dark), var(--accent-light), var(--accent));
  }
  .edge-bar.top { top: 0; }
  .edge-bar.bottom { bottom: 0; }
  .hero-photo { position: absolute; left: 0; top: 20px; width: 840px; height: 640px; }
  .headline { position: absolute; top: 708px; width: 100%; text-align: center; }
  .headline .kicker {
    font-weight: 300; font-size: 54px; letter-spacing: 2px;
    color: var(--accent); line-height: 1; white-space: nowrap;
  }
  .headline .title {
    margin-top: 8px;
    font-weight: 400; font-size: 96px; letter-spacing: 0; line-height: 1;
    white-space: nowrap;
    transform: scaleX(0.9);
    background: linear-gradient(180deg, var(--accent-light) 0%, var(--accent) 55%, var(--accent-dark) 100%);
    -webkit-background-clip: text; background-clip: text; color: transparent;
  }
  .headline .reflection {
    height: 28px; margin: 4px auto 0; width: 700px;
    background: linear-gradient(180deg, rgba(47,166,234,0.22), rgba(47,166,234,0));
    filter: blur(6px);
  }
  .offer {
    position: absolute; top: 922px; width: 100%; text-align: center;
    font-family: "Montserrat", sans-serif; font-weight: 500;
    font-size: 43px; letter-spacing: 3px; color: var(--text);
    white-space: nowrap; line-height: 1.1;
  }
  .info { position: absolute; left: 100px; width: 640px; top: 1006px; text-align: center; }
  .info .rule {
    height: 2px;
    background: linear-gradient(90deg, rgba(47,166,234,0.2), var(--accent-light), rgba(47,166,234,0.2));
  }
  .info .audience {
    padding: 13px 0 10px; font-size: 30px; letter-spacing: 5px; font-weight: 300;
    color: var(--text); white-space: nowrap;
  }
  .info .contact {
    padding: 12px 0 10px; font-size: 19px; letter-spacing: 4px; font-weight: 300;
    color: var(--text-soft); white-space: nowrap;
  }
  .info .contact .sep { margin: 0 10px; }
  .web {
    position: absolute; top: 1130px; width: 100%; text-align: center;
    font-family: "Montserrat", sans-serif; font-weight: 700;
    font-size: 22px; letter-spacing: 5px; color: var(--text); white-space: nowrap;
  }
</style>
</head>
<body>
<main class="flyer">
  <div class="edge-bar top"></div>

  <svg class="hero-photo" viewBox="0 0 840 640" role="img" aria-label="Foto in Farbspritzer-Form: Inlineskater springt vor blauem Himmel über eine Skatepark-Rampe, Bäume im Hintergrund">
    <defs>
      <linearGradient id="heroFill" x1="0" y1="0" x2="0" y2="1">
        <stop offset="0" stop-color="#8cc3ec"/>
        <stop offset="0.45" stop-color="#cfe3f4"/>
        <stop offset="0.68" stop-color="#35513a"/>
        <stop offset="0.82" stop-color="#8d959c"/>
        <stop offset="1" stop-color="#2a3540"/>
      </linearGradient>
    </defs>
    <path fill="url(#heroFill)" d="M60 160 C90 110 150 130 200 100 C250 70 330 95 380 80 C440 62 520 90 580 75 C640 60 700 110 740 150 C780 190 760 240 790 290 C810 330 770 380 760 430 C750 480 700 520 660 560 C620 600 560 580 500 610 C440 630 380 600 320 620 C260 635 210 600 170 560 C130 520 100 470 110 420 C118 380 60 360 40 320 C20 280 50 240 40 210 C35 190 45 175 60 160 Z"/>
    <g fill="#1f2327" opacity="0.9">
      <circle cx="90" cy="95" r="9"/><circle cx="790" cy="120" r="6"/>
      <circle cx="60" cy="460" r="7"/><circle cx="800" cy="480" r="5"/>
    </g>
    <g fill="#c9d3dc" opacity="0.6">
      <circle cx="40" cy="140" r="5"/><circle cx="770" cy="60" r="4"/>
      <circle cx="55" cy="400" r="6"/><circle cx="815" cy="380" r="4"/>
    </g>
  </svg>

  <header class="headline">
    <div class="kicker">AGGRESSIVE</div>
    <h1 class="title">INLINE SKATING</h1>
    <div class="reflection"></div>
  </header>

  <h2 class="offer">PROFESSIONELLES TRAINING</h2>

  <section class="info">
    <div class="rule"></div>
    <p class="audience">FÜR KINDER UND JUGENDLICHE</p>
    <div class="rule"></div>
    <p class="contact">BEN LORAK<span class="sep">|</span>BENIMIX2004@NORDPOST.DE</p>
    <div class="rule"></div>
  </section>

  <p class="web">WWW.FLIMMORA.COM/USER/BELURAKSCHER1</p>

  <div class="edge-bar bottom"></div>
</main>
</body>
</html>
```